Tattoo Artist needs a personal business card designed

I am looking for a classy, clean, but antique feeling business card for myself that matches the theme and vibe of my tattoo shop. I would like to see a couple different options but we can go with an all black background, to start. I would like to see some western metallic lettering and deep/dark red accents. Maybe try adding a few with a mix of white fonts too. I would like to see the Shop's name and location which is Copper Lantern Ink, 4862 W. Delmora Rd. Tampa FL. 33617 Our tattoo shop has a western antique vibe, yet its classy and professional. We have a website you can see the color scheme and grab anymore information for designing this business card from: www.copperlanternink-studio.example - and if you want to add the website to the card. I would like my personal IG handle somewhere small with a unique and cleaner IG logo next to the name. My IG handle is: @dianekessoink I am basically trying to look for multiple ideas/concepts that will match best with our website and sticker. (Which I will upload in the files) I would like it to be very clean, simple, classy, but have a western traditional tattooing feel to it. Like an antique stores business card. Add whatever information you think would be best, since I am not the professional graphic designer.
Shop Name: Copper Lantern Ink
Location: 4862 W Delmora Rd Tampa FL 33617
Website: www.copperlanternink-studio.example
Number: 813 555 0187
My Personal IG: @dianekessoink

Thank you for taking your time to help me out with this project. Afterwards, I might need our studios website up for re-designing! So my end goal is to make everything intergraded with one another. I more likely need a logo too.

Target Market(s)

Professionals 35-55 years of age Male and Female
Firefighters, Military Service men and women

Contact Information for Business Card

All black background, with golden and red accents.
Traditional style, cowboy, western. Sharp, Clean, and Classy.

Requirements
Must have
• Shop Name - Copper Lantern Ink
• Shop Location - 4862 W Delmora Rd Tampa FL 33617
• My Name - Diane Kesso
• UNIQUE IG LOGO along with My Instagram - @dianekessoink
• Number - 813 555 0187
Nice to have
• Gold metallic font
• Red accents
• Western Antique Oddity feel
• Might be nice to have the Website if it can work and fit in the space.

```html
<!DOCTYPE html>
<html lang="en">
<head>
<meta charset="utf-8">
<title>Diane Kesso – Business Card</title>
<link rel="stylesheet" href="https://fonts.googleapis.com/css2?family=Open+Sans:wght@400;600;700&family=Parisienne&display=swap">
<style>
  :root {
    --backdrop: #2e2824;
    --card: #141414;
    --card-edge: #0c0c0c;
    --ink-red: #a3262b;
    --gold: #c9922f;
    --gold-light: #e0b25a;
    --bronze: #8a5a24;
    --text-white: #f2f2f2;
  }
  * { margin: 0; padding: 0; box-sizing: border-box; }
  html, body {
    width: 1200px;
    height: 672px;
    overflow: hidden;
    background: var(--backdrop);
  }
  .canvas {
    position: relative;
    width: 1200px;
    height: 672px;
    display: flex;
    justify-content: center;
    align-items: center;
    gap: 60px;
  }
  .card {
    position: relative;
    width: 320px;
    height: 560px;
    background: var(--card);
    border: 1px solid var(--card-edge);
    box-shadow: 0 10px 28px rgba(0,0,0,0.45);
    overflow: hidden;
  }

  /* Contact side */
  .artist-name {
    position: absolute;
    left: 40px;
    top: 234px;
    font-family: "Parisienne", cursive;
    font-weight: 400;
    font-size: 31px;
    line-height: 1.2;
    color: var(--ink-red);
  }
  .contact-list {
    position: absolute;
    left: 44px;
    right: 14px;
    top: 292px;
    list-style: none;
    font-family: "Open Sans", sans-serif;
    font-size: 12.5px;
    color: var(--text-white);
  }
  .contact-list li {
    display: flex;
    align-items: center;
    gap: 9px;
    height: 24px;
    white-space: nowrap;
  }
  .contact-list .icon { width: 12px; height: 12px; flex: none; }
  .contact-list .address { margin-top: 18px; }

  /* Shop side */
  .shop-emblem {
    position: absolute;
    left: 0;
    right: 0;
    top: 140px;
    display: flex;
    flex-direction: column;
    align-items: center;
  }
  .emblem-art {
    width: 270px;
    height: 190px;
    border-radius: 50% 50% 46% 46%;
    background:
      radial-gradient(ellipse at 50% 22%, rgba(240,236,220,0.55) 0 8%, transparent 16%),
      radial-gradient(ellipse at 50% 55%, var(--bronze) 0%, rgba(138,90,36,0.75) 35%, rgba(201,146,47,0.35) 60%, transparent 72%);
  }
  .shop-name {
    margin-top: 6px;
    font-family: "Open Sans", sans-serif;
    font-weight: 700;
    font-size: 24px;
    letter-spacing: 1.5px;
    text-transform: uppercase;
    color: var(--gold);
    text-align: center;
    line-height: 1.25;
  }
</style>
</head>
<body>
<main class="canvas">
  <section class="card card-contact" aria-label="Contact side">
    <h1 class="artist-name">Diane Kesso</h1>
    <ul class="contact-list">
      <li>
        <svg class="icon" viewBox="0 0 12 12" aria-hidden="true"><rect x="3" y="0.8" width="6" height="10.4" rx="1" fill="none" stroke="var(--gold)" stroke-width="1.3"/><circle cx="6" cy="9.2" r="0.7" fill="var(--gold)"/></svg>
        <span>813 555 0187</span>
      </li>
      <li>
        <svg class="icon" viewBox="0 0 12 12" aria-hidden="true"><g fill="none" stroke="var(--gold)" stroke-width="1"><circle cx="6" cy="6" r="5"/><ellipse cx="6" cy="6" rx="2.2" ry="5"/><line x1="1" y1="6" x2="11" y2="6"/></g></svg>
        <span>www.copperlanternink-studio.example</span>
      </li>
      <li>
        <svg class="icon" viewBox="0 0 12 12" aria-hidden="true"><rect x="1" y="1" width="10" height="10" rx="0" fill="var(--gold)"/></svg>
        <span>@dianekessoink</span>
      </li>
      <li class="address"><span>4862 W Delmora Rd Tampa FL 33617</span></li>
    </ul>
  </section>

  <section class="card card-shop" aria-label="Shop side">
    <div class="shop-emblem">
      <div class="emblem-art" role="img" aria-label="Shop emblem illustration: spread-winged bird in bronze and gold beneath a glowing starburst, framed by antique gold scrollwork"></div>
      <p class="shop-name">Copper Lantern Ink</p>
    </div>
  </section>
</main>
</body>
</html>
```